TrueGrindz Complete Stationery - Logo already designed

I already have the logo designed see attached. I need have a full set of stationary and business card designed for printing. I have attached an example of what I mean.

Please feel free to be creative. Also you can use the X in the logo by its self if you think it will work.

My details:

Name: Corwin Lestak
Social media handles: @corwinlestak
W: corwinlestak.com
E: info@corwinlestak.com
​P: 08 7493 5286
PO Box 7382, Harrowdale 6027
ABN 83 402 719 265

Target Market(s)

Anyone looking to be inspired.

Industry/Entity Type

Business

Font styles to use
Sans Serif

Colors
fbee3e
000000

Requirements
Must have
• My details:
• Name: Corwin Lestak
• Social media handles: @corwinlestak
• W: corwinlestak.com
• E: info@corwinlestak.com
• ​P: 08 7493 5286
• PO Box 7382, Harrowdale 6027
• ABN 83 402 719 265
Nice to have
• Something a little different
Should not have
• must not look tacky.

```html
<!DOCTYPE html>
<html lang="en">
<head>
<meta charset="utf-8">
<title>TrueGrindz Stationery Set</title>
<link href="https://fonts.googleapis.com/css2?family=Roboto:wght@400;500;700&display=swap" rel="stylesheet">
<style>
  :root {
    --board: #858384;
    --ink: #231f20;
    --paper: #ffffff;
    --yellow: #fbcf0a;
    --grey-text: #333333;
    --spine: #3a3637;
  }
  * { margin: 0; padding: 0; box-sizing: border-box; }
  html, body { width: 1189px; height: 1200px; overflow: hidden; }
  body {
    background: var(--board);
    font-family: "Roboto", Arial, sans-serif;
    color: var(--grey-text);
    position: relative;
  }
  .item { position: absolute; overflow: hidden; }
  .brand-name { font-family: "Roboto", Arial, sans-serif; font-weight: 700; letter-spacing: -0.5px; line-height: 1; position: absolute; white-space: nowrap; }
  .on-dark { color: var(--paper); }
  .on-light { color: var(--ink); }
  .web-link { position: absolute; color: var(--yellow); white-space: nowrap; }
  .footer-band { position: absolute; left: 0; right: 0; bottom: 0; }
  .footer-band .band-dark { position: absolute; left: 0; bottom: 0; background: var(--ink); }
  .footer-band .band-yellow { position: absolute; right: 0; bottom: 0; top: 0; background: var(--yellow); color: var(--ink); display: flex; align-items: center; justify-content: flex-end; }
  .social-row { position: absolute; display: flex; }
  .social-row span { border: 1px solid var(--yellow); border-radius: 50%; display: block; }
  .handle { position: absolute; color: var(--grey-text); white-space: nowrap; }
  .contact { position: absolute; white-space: nowrap; color: var(--grey-text); }
  .contact .label { color: var(--yellow); }

  /* Presentation folder */
  .folder { left: 115px; top: 82px; width: 420px; height: 542px; background: var(--ink); }
  .folder .spine { position: absolute; left: 13px; top: 0; bottom: 0; width: 2px; background: var(--spine); }
  .folder .web-link { right: 28px; top: 36px; font-size: 7.5px; }
  .folder .brand-name { right: 28px; top: 476px; font-size: 37px; }

  /* Letterhead */
  .letterhead { left: 639px; top: 86px; width: 419px; height: 541px; background: var(--paper); }
  .letterhead .brand-name { left: 34px; top: 37px; font-size: 34px; }
  .letterhead .social-row { left: 311px; top: 31px; gap: 6px; }
  .letterhead .social-row span { width: 14px; height: 14px; }
  .letterhead .handle { left: 324px; top: 48px; font-size: 7px; }
  .letterhead .contact { left: 35px; top: 108px; font-size: 7px; line-height: 9.5px; padding-left: 6px; border-left: 1px solid var(--ink); }
  .recipient { position: absolute; left: 35px; top: 187px; font-size: 7px; line-height: 8.5px; color: var(--grey-text); }
  .recipient strong { display: block; font-size: 8.5px; font-weight: 500; color: var(--ink); margin-bottom: 4px; letter-spacing: 0.3px; }
  .letter-body { position: absolute; left: 35px; top: 244px; width: 352px; font-size: 7.3px; line-height: 12.3px; color: var(--grey-text); }
  .letter-body p + p { margin-top: 12px; }
  .sign-off { position: absolute; left: 35px; top: 408px; font-size: 7px; }
  .signature-area { position: absolute; left: 35px; top: 426px; width: 100px; height: 32px; background: linear-gradient(90deg, #e6e6e6, #f4f4f4); }
  .signer { position: absolute; left: 35px; top: 463px; font-size: 7.5px; line-height: 9.5px; }
  .signer strong { font-weight: 500; color: var(--ink); display: block; font-size: 8px; }
  .letterhead .footer-band { height: 16px; }
  .letterhead .band-dark { width: 265px; height: 11px; clip-path: polygon(0 0, 100% 0, 96% 100%, 0 100%); }
  .letterhead .band-yellow { left: 258px; font-size: 7px; padding-right: 14px; clip-path: polygon(4% 0, 100% 0, 100% 100%, 0 100%); }

  /* DL envelope front */
  .envelope-front { left: 115px; top: 678px; width: 364px; height: 182px; background: var(--paper); }
  .envelope-front .brand-name { left: 13px; top: 22px; font-size: 27px; }
  .envelope-front .contact { left: 13px; top: 128px; font-size: 6px; line-height: 8px; }
  .envelope-front .social-row { left: 270px; top: 134px; gap: 7px; }
  .envelope-front .social-row span { width: 13px; height: 13px; }
  .envelope-front .handle { left: 285px; top: 152px; font-size: 6px; }
  .envelope-front .footer-band { height: 15px; }
  .envelope-front .band-dark { width: 230px; height: 8px; clip-path: polygon(0 0, 100% 0, 97% 100%, 0 100%); }
  .envelope-front .band-yellow { left: 223px; font-size: 6px; padding-right: 44px; clip-path: polygon(4% 0, 100% 0, 100% 100%, 0 100%); }

  /* DL envelope back */
  .envelope-back { left: 115px; top: 920px; width: 364px; height: 182px; background: var(--paper); }
  .envelope-back .flap { position: absolute; left: 0; top: 0; width: 364px; height: 51px; background: var(--ink); clip-path: polygon(0 0, 100% 0, 98% 100%, 2% 100%); }
  .envelope-back .brand-name { left: 50%; top: 17px; transform: translateX(-50%); font-size: 15px; color: var(--yellow); }

  /* USB drives */
  .usb { top: 675px; height: 51px; }
  .usb-light { left: 758px; width: 129px; background: var(--paper); }
  .usb-light .cap { position: absolute; right: 0; top: 3px; bottom: 3px; width: 24px; background: var(--ink); }
  .usb-dark { left: 923px; width: 131px; background: var(--ink); }
  .usb-dark .cap { position: absolute; right: 0; top: 3px; bottom: 3px; width: 22px; background: var(--paper); }
  .usb .brand-name { top: 19px; font-size: 12px; color: var(--yellow); }
  .usb-light .brand-name { left: 20px; }
  .usb-dark .brand-name { left: 28px; }

  /* Business card back */
  .card-back { left: 525px; top: 769px; width: 273px; height: 154px; background: var(--ink); }
  .card-back .web-link { right: 15px; top: 21px; font-size: 7.5px; }
  .card-back .brand-name { right: 15px; top: 125px; font-size: 23px; }

  /* Business card front */
  .card-front { left: 526px; top: 948px; width: 268px; height: 154px; background: var(--paper); }
  .card-front .brand-name { left: 14px; top: 24px; font-size: 36px; }
  .card-name { position: absolute; left: 14px; top: 77px; font-size: 10.5px; font-weight: 500; color: var(--ink); letter-spacing: 0.4px; }
  .card-front .contact { left: 14px; top: 94px; font-size: 7.8px; line-height: 12.2px; }
  .card-front .social-row { left: 176px; top: 99px; gap: 8px; }
  .card-front .social-row span { width: 14px; height: 14px; }
  .card-front .handle { left: 191px; top: 117px; font-size: 7.5px; }
  .card-front .footer-band { height: 12px; }
  .card-front .band-dark { width: 170px; height: 7px; clip-path: polygon(0 0, 100% 0, 96% 100%, 0 100%); }
  .card-front .band-yellow { left: 163px; font-size: 7px; padding-right: 26px; clip-path: polygon(5% 0, 100% 0, 100% 100%, 0 100%); }

  /* Notebook */
  .notebook { left: 864px; top: 823px; width: 200px; height: 278px; background: var(--ink); }
  .notebook .web-link { right: 14px; top: 18px; font-size: 3.5px; }
  .notebook .brand-name { right: 13px; top: 239px; font-size: 21px; }
</style>
</head>
<body>

  <section class="item folder" aria-label="Presentation folder">
    <div class="spine"></div>
    <span class="web-link">corwinlestak.com</span>
    <span class="brand-name on-dark">TrueGrindz</span>
  </section>

  <section class="item letterhead" aria-label="Letterhead">
    <span class="brand-name on-light">TrueGrindz</span>
    <div class="social-row"><span></span><span></span><span></span><span></span></div>
    <span class="handle">@corwinlestak</span>
    <div class="contact">
      PO Box 7382, Harrowdale 6027<br>
      <span class="label">P:</span> 08 7493 5286<br>
      <span class="label">E:</span> info@corwinlestak.com<br>
      ABN 83 402 719 265
    </div>
    <div class="recipient">
      <strong>DANA WHITLOW</strong>
      Street Name,City Name.<br>
      Zip Coad 0000
    </div>
    <div class="letter-body">
      <p>Lorem Ipsum is simply dummy text of the printing and typesetting industry. Lorem Ipsum has been the industry's standard dummy text ever since the 1500s, when an unknown printer took a galley of type and scrambled it to make a type specimen book. It has survived not only five centuries,but also the leap into electronic typesetting, remaining essentially unchanged. It was popularised in the 1960s with the release of Letraset sheets containing Lorem Ipsum passages, and more recently with desktop publishing software like Aldus PageMaker including versions of Lorem Ipsum.</p>
      <p>It is a long established fact that a reader will be distracted by the readable content of a page when looking at its layout. The point of using Lorem Ipsum is that it has a more-or-less normal distribution of letters, as opposed to using 'Content here, content here', making it look like readable English. Many desktop and at years, sometimes by accident, sometimes on purpose (injected humour and the like).</p>
    </div>
    <span class="sign-off">Regards,</span>
    <div class="signature-area" role="img" aria-label="Handwritten signature of Marcus Hale"></div>
    <div class="signer"><strong>Marcus Hale</strong>General Maneger</div>
    <div class="footer-band">
      <div class="band-dark"></div>
      <div class="band-yellow">corwinlestak.com</div>
    </div>
  </section>

  <section class="item envelope-front" aria-label="DL envelope front">
    <span class="brand-name on-light">TrueGrindz</span>
    <div class="contact">
      PO Box 7382, Harrowdale 6027<br>
      <span class="label">P:</span> 08 7493 5286<br>
      <span class="label">E:</span> info@corwinlestak.com<br>
      ABN 83 402 719 265
    </div>
    <div class="social-row"><span></span><span></span><span></span><span></span></div>
    <span class="handle">@corwinlestak</span>
    <div class="footer-band">
      <div class="band-dark"></div>
      <div class="band-yellow">corwinlestak.com</div>
    </div>
  </section>

  <section class="item envelope-back" aria-label="DL envelope back">
    <div class="flap"></div>
    <span class="brand-name">TrueGrindz</span>
  </section>

  <section class="item usb usb-light" aria-label="USB drive, white">
    <span class="brand-name">TrueGrindz</span>
    <div class="cap"></div>
  </section>
  <section class="item usb usb-dark" aria-label="USB drive, black">
    <span class="brand-name">TrueGrindz</span>
    <div class="cap"></div>
  </section>

  <section class="item card-back" aria-label="Business card back">
    <span class="web-link">corwinlestak.com</span>
    <span class="brand-name on-dark">TrueGrindz</span>
  </section>

  <section class="item card-front" aria-label="Business card front">
    <span class="brand-name on-light">TrueGrindz</span>
    <span class="card-name">CORWIN LESTAK</span>
    <div class="contact">
      PO Box 7382, Harrowdale 6027<br>
      <span class="label">P:</span> 08 7493 5286<br>
      <span class="label">E:</span> info@corwinlestak.com<br>
      ABN 83 402 719 265
    </div>
    <div class="social-row"><span></span><span></span><span></span><span></span></div>
    <span class="handle">@corwinlestak</span>
    <div class="footer-band">
      <div class="band-dark"></div>
      <div class="band-yellow">corwinlestak.com</div>
    </div>
  </section>

  <section class="item notebook" aria-label="Notebook cover">
    <span class="web-link">corwinlestak.com</span>
    <span class="brand-name on-dark">TrueGrindz</span>
  </section>

</body>
</html>
```